Ridgeway College 2016 ATAR results

We are a private college, providing Foundation to Year 12 education. We are very diverse. Our motto is 'Excellence, Innovation, Diversity'. We are an academic school, and very diverse. This is our third year of year 12 graduates. In 2014, we had one student out of seven who achieved 99.15. In 2015, we had two students also out of seven who achieved 99.7 and 96.3. This year we are hoping to have 3 students who will also receive their scores in the high 90's.

Target Market(s)

all audience, to promote the school's success.

Industry/Entity Type

Education

Font styles to use
Serif

Requirements
Must have
• 1. College logo, 2. college moto "Excellence, Innovation, Diversity"
• 3. Photos of the students that have received the high ATAR Scores
• 4. The current calendar year. An indication that these are the ATAR scores for this year.
• 5. The college website
• 6. The file to be editable by us, as we are not going to know exactly, what scores the students are going to have, and in what order. We need the file to be editable, so we have the flexibility of doing last minute changes.
Nice to have
• Nice design that's eye catching and stands out. As it's only our third year and we are expecting few students to achieve high ATAR Scores, the design needs to be eye catching and kind of celebrating the success.
Should not have
• Can't think of anything at this stage.

```html
<!DOCTYPE html>
<html lang="en">
<head>
<meta charset="utf-8">
<title>Ridgeway College – Year 12 2016 ATAR Results</title>
<link rel="stylesheet" href="https://fonts.googleapis.com/css2?family=Josefin+Sans:wght@600;700&family=Abril+Fatface&family=Lora:wght@600;700&display=swap">
<style>
  :root {
    --page-bg: #f2f2f2;
    --frame: #2f3132;
    --orange-light: #f2917a;
    --orange-mid: #ec7b5d;
    --orange-deep: #e4633f;
    --rod: #333536;
    --rod-band: #f6a58e;
    --photo-sky-top: #a9c6e6;
    --photo-sky-bottom: #5d8fc9;
    --gown: #1e1e22;
    --sash: #d9a21f;
    --ink: #2a2420;
    --excellence: #b5b7cf;
    --innovation: #f5f1c6;
    --diversity: #f0561c;
    --logo-bg: #ffffff;
    --logo-text: #2d3a8c;
    --web: #fbe9e2;
    --caption: #fff4ee;
    --year-red: #b32a26;
    --ribbon: #d7eee0;
    --date: #7a2a22;
  }
  * { margin: 0; padding: 0; box-sizing: border-box; }
  html, body { width: 1078px; height: 1200px; overflow: hidden; background: var(--page-bg); }
  .poster {
    position: absolute; left: 106px; top: 0;
    width: 865px; height: 1200px;
    background: var(--frame);
  }
  .poster-field {
    position: absolute; left: 32px; top: 44px; width: 799px; height: 1111px;
    background: radial-gradient(ellipse at 45% 40%, var(--orange-light) 0%, var(--orange-mid) 55%, var(--orange-deep) 100%);
    overflow: hidden;
  }
  .portrait { position: absolute; width: 220px; height: 250px; }
  .portrait .rod { position: absolute; left: 0; top: 0; width: 220px; height: 14px; }
  .portrait .band {
    position: absolute; left: 28px; top: 9px; width: 162px; height: 8px;
    background: var(--rod-band);
  }
  .portrait .photo {
    position: absolute; left: 28px; top: 14px; width: 162px; height: 192px;
    background: linear-gradient(180deg, var(--photo-sky-top) 0%, var(--photo-sky-bottom) 60%, var(--gown) 60%, var(--gown) 78%, var(--sash) 78%, var(--gown) 100%);
  }
  .portrait .caption {
    position: absolute; left: 18px; top: 209px; width: 182px; text-align: center;
    font-family: "Lora", serif; color: var(--caption); line-height: 1.15;
  }
  .caption .student-name { display: block; font-weight: 600; font-size: 14px; }
  .caption .student-score { display: block; font-weight: 700; font-size: 16px; letter-spacing: 0.5px; color: var(--ink); }
  .motto {
    position: absolute;
    writing-mode: vertical-rl; text-orientation: upright;
    font-family: "Josefin Sans", sans-serif; font-weight: 700;
    font-size: 58px; letter-spacing: 2px; line-height: 1;
    -webkit-text-stroke: 2px var(--ink);
    paint-order: stroke fill;
  }
  .motto-excellence { left: 291px; top: 94px; color: var(--excellence); }
  .motto-innovation { left: 378px; top: 213px; color: var(--innovation); }
  .motto-diversity { left: 465px; top: 346px; color: var(--diversity); }
  .brand {
    position: absolute; left: 552px; top: 44px; width: 247px; height: 99px;
    background: var(--logo-bg); border-radius: 22px 0 0 22px;
    display: flex; align-items: center; gap: 10px; padding-left: 18px;
  }
  .brand-dot { width: 18px; height: 18px; border-radius: 50%; background: var(--logo-text); flex: none; }
  .brand-name {
    font-family: "Lora", serif; font-weight: 700; font-size: 28px;
    line-height: 1.05; color: var(--logo-text);
  }
  .website {
    position: absolute; left: 548px; top: 149px; width: 251px; text-align: center;
    font-family: "Josefin Sans", sans-serif; font-weight: 600; font-size: 16px;
    letter-spacing: 1.4px; color: var(--web);
  }
  .results-label {
    position: absolute; left: 290px; top: 900px; width: 170px; text-align: center;
    font-family: "Lora", serif; font-weight: 700; font-size: 19px; letter-spacing: 2px;
    color: var(--caption);
  }
  .year-badge { position: absolute; left: 316px; top: 950px; width: 180px; height: 160px; }
  .year-number {
    position: absolute; left: 30px; top: -8px; width: 120px; text-align: center;
    font-family: "Abril Fatface", serif; font-size: 140px; line-height: 1;
    color: var(--year-red);
  }
  .year-ribbon { position: absolute; left: 5px; top: 100px; width: 175px; height: 40px; }
  .year-label {
    position: absolute; left: 5px; top: 106px; width: 175px; text-align: center;
    font-family: "Lora", serif; font-weight: 600; font-size: 18px; letter-spacing: 1px; color: var(--ink);
  }
  .year-date {
    position: absolute; left: 5px; top: 136px; width: 175px; text-align: center;
    font-family: "Lora", serif; font-weight: 600; font-size: 22px; color: var(--date);
  }
</style>
</head>
<body>
<div class="poster">
  <div class="poster-field">
    <div class="portrait" style="left:26px; top:24px;">
      <div class="band"></div>
      <svg class="rod" viewBox="0 0 220 14"><line x1="10" y1="7" x2="210" y2="7" stroke="var(--rod)" stroke-width="5"/><ellipse cx="7" cy="7" rx="7" ry="5" fill="var(--rod)"/><ellipse cx="213" cy="7" rx="7" ry="5" fill="var(--rod)"/></svg>
      <div class="photo" role="img" aria-label="Portrait of graduating student in cap, gown and gold sash"></div>
      <p class="caption"><span class="student-name">Student Name</span><span class="student-score">ATAR 00.00</span></p>
    </div>
    <div class="portrait" style="left:26px; top:303px;">
      <div class="band"></div>
      <svg class="rod" viewBox="0 0 220 14"><line x1="10" y1="7" x2="210" y2="7" stroke="var(--rod)" stroke-width="5"/><ellipse cx="7" cy="7" rx="7" ry="5" fill="var(--rod)"/><ellipse cx="213" cy="7" rx="7" ry="5" fill="var(--rod)"/></svg>
      <div class="photo" role="img" aria-label="Portrait of graduating student in cap, gown and gold sash"></div>
      <p class="caption"><span class="student-name">Student Name</span><span class="student-score">ATAR 00.00</span></p>
    </div>
    <div class="portrait" style="left:26px; top:586px;">
      <div class="band"></div>
      <svg class="rod" viewBox="0 0 220 14"><line x1="10" y1="7" x2="210" y2="7" stroke="var(--rod)" stroke-width="5"/><ellipse cx="7" cy="7" rx="7" ry="5" fill="var(--rod)"/><ellipse cx="213" cy="7" rx="7" ry="5" fill="var(--rod)"/></svg>
      <div class="photo" role="img" aria-label="Portrait of graduating student in cap, gown and gold sash"></div>
      <p class="caption"><span class="student-name">Student Name</span><span class="student-score">ATAR 00.00</span></p>
    </div>
    <div class="portrait" style="left:26px; top:855px;">
      <div class="band"></div>
      <svg class="rod" viewBox="0 0 220 14"><line x1="10" y1="7" x2="210" y2="7" stroke="var(--rod)" stroke-width="5"/><ellipse cx="7" cy="7" rx="7" ry="5" fill="var(--rod)"/><ellipse cx="213" cy="7" rx="7" ry="5" fill="var(--rod)"/></svg>
      <div class="photo" role="img" aria-label="Portrait of graduating student in cap, gown and gold sash"></div>
      <p class="caption"><span class="student-name">Student Name</span><span class="student-score">ATAR 00.00</span></p>
    </div>
    <div class="portrait" style="left:554px; top:303px;">
      <div class="band"></div>
      <svg class="rod" viewBox="0 0 220 14"><line x1="10" y1="7" x2="210" y2="7" stroke="var(--rod)" stroke-width="5"/><ellipse cx="7" cy="7" rx="7" ry="5" fill="var(--rod)"/><ellipse cx="213" cy="7" rx="7" ry="5" fill="var(--rod)"/></svg>
      <div class="photo" role="img" aria-label="Portrait of graduating student in cap, gown and gold sash"></div>
      <p class="caption"><span class="student-name">Student Name</span><span class="student-score">ATAR 00.00</span></p>
    </div>
    <div class="portrait" style="left:554px; top:586px;">
      <div class="band"></div>
      <svg class="rod" viewBox="0 0 220 14"><line x1="10" y1="7" x2="210" y2="7" stroke="var(--rod)" stroke-width="5"/><ellipse cx="7" cy="7" rx="7" ry="5" fill="var(--rod)"/><ellipse cx="213" cy="7" rx="7" ry="5" fill="var(--rod)"/></svg>
      <div class="photo" role="img" aria-label="Portrait of graduating student in cap, gown and gold sash"></div>
      <p class="caption"><span class="student-name">Student Name</span><span class="student-score">ATAR 00.00</span></p>
    </div>
    <div class="portrait" style="left:556px; top:855px;">
      <div class="band"></div>
      <svg class="rod" viewBox="0 0 220 14"><line x1="10" y1="7" x2="210" y2="7" stroke="var(--rod)" stroke-width="5"/><ellipse cx="7" cy="7" rx="7" ry="5" fill="var(--rod)"/><ellipse cx="213" cy="7" rx="7" ry="5" fill="var(--rod)"/></svg>
      <div class="photo" role="img" aria-label="Portrait of graduating student in cap, gown and gold sash"></div>
      <p class="caption"><span class="student-name">Student Name</span><span class="student-score">ATAR 00.00</span></p>
    </div>

    <div class="motto motto-excellence">EXCELLENCE</div>
    <div class="motto motto-innovation">INNOVATION</div>
    <div class="motto motto-diversity">DIVERSITY</div>

    <div class="brand">
      <span class="brand-dot"></span>
      <span class="brand-name">Ridgeway<br>College</span>
    </div>
    <div class="website">www.ridgeway.sa.edu.au</div>

    <div class="results-label">ATAR RESULTS</div>
    <div class="year-badge">
      <div class="year-number">12</div>
      <svg class="year-ribbon" viewBox="0 0 175 40">
        <polygon points="0,30 22,14 22,34" fill="var(--ribbon)"/>
        <polygon points="175,30 153,14 153,34" fill="var(--ribbon)"/>
        <path d="M22,8 Q88,-4 153,8 L153,30 Q88,18 22,30 Z" fill="var(--ribbon)" stroke="var(--ink)" stroke-width="1"/>
      </svg>
      <div class="year-label">YEAR</div>
      <div class="year-date">2016</div>
    </div>
  </div>
</div>
</body>
</html>
```